Boring Fiberglass Repair Company needs creative business cards

The Fiberglass Repair industry isn't very fun or creative but we'd like a business card that communicates a fresh, modern, and service-oriented feel. We repair bathroom fixtures (bath tubs, showers, etc) which are made out of fiberglass. Our fiberglass repair service will be sold to bathtub manufacturers and also businesses that sell bathtubs. We will also offer our services to home owners that have broken showers and bathtubs.
Target Market(s)
Home builders, plumbing wholesalers, home owners
Contact Information for Business Card
Name
Phone Number
Email Address
Business Address
Tag line: "Quality Craftsmanship Today"

```html
<!DOCTYPE html>
<html lang="en">
<head>
<meta charset="utf-8">
<title>Ridgeline Fiberglass – Business Card</title>
<link rel="stylesheet" href="https://fonts.googleapis.com/css2?family=Montserrat:wght@400;500;700&display=swap">
<style>
  :root {
    --backdrop: #8c8c8e;
    --card-navy: #0f2150;
    --card-edge: #8a1414;
    --ink-white: #ffffff;
    --ink-soft: #dfe5f2;
    --brand-blue: #1f8fe8;
  }
  * { box-sizing: border-box; margin: 0; padding: 0; }
  html, body {
    width: 1200px; height: 800px; overflow: hidden;
    background: var(--backdrop);
    font-family: "Montserrat", Arial, sans-serif;
  }
  .canvas {
    position: relative; width: 1200px; height: 800px;
    display: flex; align-items: center; justify-content: center; gap: 60px;
  }
  .card {
    position: relative;
    width: 525px; height: 300px;
    background: var(--card-navy);
    border-bottom: 3px solid var(--card-edge);
    border-right: 2px solid var(--card-edge);
    box-shadow: 0 18px 30px rgba(0,0,0,.28);
  }

  /* Contact side */
  .card--contact { color: var(--ink-white); }
  .contact-row {
    position: absolute; top: 96px; left: 0; right: 0;
    display: flex; justify-content: center; align-items: center; gap: 18px;
  }
  .identity { text-align: right; }
  .identity__name {
    font-weight: 700; font-size: 20px; letter-spacing: .5px;
    text-transform: uppercase;
  }
  .identity__address { font-size: 12.5px; line-height: 1.35; margin-top: 3px; color: var(--ink-soft); }
  .divider { width: 1px; height: 62px; background: var(--ink-soft); opacity: .8; }
  .channels { list-style: none; font-size: 12.5px; line-height: 1.6; color: var(--ink-soft); }
  .channels li { display: flex; align-items: center; gap: 8px; }
  .channels svg { width: 11px; height: 11px; flex: none; }
  .icon-fill { fill: var(--ink-white); }
  .icon-line { fill: none; stroke: var(--ink-white); stroke-width: 2; }
  .tagline {
    position: absolute; bottom: 62px; left: 0; right: 0; text-align: center;
    font-weight: 500; font-size: 15px; letter-spacing: 1.4px; text-transform: uppercase;
  }

  /* Brand side */
  .card--brand { display: flex; align-items: center; justify-content: center; }
  .brand-name {
    color: var(--brand-blue);
    font-weight: 700; font-size: 34px; line-height: 1;
  }
</style>
</head>
<body>
<main class="canvas">
  <section class="card card--contact" aria-label="Contact side">
    <div class="contact-row">
      <div class="identity">
        <p class="identity__name">Daniel Reyes</p>
        <p class="identity__address">412 Birchwood Road<br>Fairbanks, Alaska 99701</p>
      </div>
      <span class="divider"></span>
      <ul class="channels">
        <li>
          <svg viewBox="0 0 24 24" aria-hidden="true"><path class="icon-fill" d="M6.6 10.8a15.1 15.1 0 0 0 6.6 6.6l2.2-2.2a1 1 0 0 1 1-.25 11.4 11.4 0 0 0 3.6.57 1 1 0 0 1 1 1V20a1 1 0 0 1-1 1A17 17 0 0 1 3 4a1 1 0 0 1 1-1h3.5a1 1 0 0 1 1 1c0 1.25.2 2.45.57 3.57a1 1 0 0 1-.25 1z"/></svg>
          555-014-2273
        </li>
        <li>
          <svg viewBox="0 0 24 24" aria-hidden="true"><rect class="icon-fill" x="2" y="5" width="20" height="14"/></svg>
          info@ridgelinefiber.com
        </li>
        <li>
          <svg viewBox="0 0 24 24" aria-hidden="true"><circle class="icon-line" cx="12" cy="12" r="9"/><path class="icon-line" d="M3 12h18M12 3c-3 3-3 15 0 18M12 3c3 3 3 15 0 18"/></svg>
          www.ridgelinefiber.com
        </li>
      </ul>
    </div>
    <p class="tagline">Quality Craftsmanship Today</p>
  </section>

  <section class="card card--brand" aria-label="Brand side">
    <p class="brand-name">Ridgeline Fiberglass</p>
  </section>
</main>
</body>
</html>
```